Ledgerway Partners, LLC
Project: Biz Card & Stationery
Biz Card & Stationery - Consulting
Biz Card & Stationery
Professional
Denise M. Holloway, CPP, PMP
Founder and CEO
4812 Linwood Avenue NE Suite 210 Atlanta, GA 30318
dholloway@ledgerway-hq.com
ledgerway-hq.com
DUNS No. 052817634 NAICS CODES: 541611 541214 541512 611430 561320

```html
<!DOCTYPE html>
<html lang="en">
<head>
<meta charset="utf-8">
<title>Ledgerway Partners, LLC – Biz Card &amp; Stationery</title>
<link href="https://fonts.googleapis.com/css2?family=Open+Sans:wght@400;600;700&display=swap" rel="stylesheet">
<style>
:root{
  --bg:#a7a9ab;
  --paper:#ffffff;
  --red:#d3202f;
  --purple:#7b3b8f;
  --ink:#3a3a3a;
  --muted:#8a8a8a;
  --faint:rgba(255,255,255,.16);
  --faint-dark:rgba(123,59,143,.08);
}
*{margin:0;padding:0;box-sizing:border-box}
html,body{width:1200px;height:240px;overflow:hidden}
body{background:var(--bg);font-family:"Open Sans",Arial,sans-serif;color:var(--ink);position:relative}
.piece{position:absolute;background:var(--paper);box-shadow:0 2px 5px rgba(0,0,0,.25);overflow:hidden}
.card{width:134px;height:90px}
.brand{display:flex;align-items:center;gap:3px;font-weight:700;font-size:6.5px;color:var(--red);white-space:nowrap}
.brand .dot{width:9px;height:9px;border-radius:50%;background:var(--purple)}
.name{font-weight:700;font-size:5.4px;color:var(--ink)}
.role{font-size:4.2px;color:var(--muted)}
.contact{font-size:4px;line-height:1.45;color:var(--ink)}
.rule{position:absolute;left:0;right:0;bottom:0;height:3px;background:var(--red)}
.rule.purple{background:var(--purple)}
.codes{position:absolute;left:10px;top:10px;color:#fff;font-size:5px;line-height:1.55;font-weight:600}
.mark-circle{position:absolute;border-radius:50%}
.card.red{background:var(--red)}
.card.purple{background:var(--purple)}
.env{width:130px;height:88px}
.flap{position:absolute;inset:0}
.page{width:150px;height:212px}
</style>
</head>
<body>

<!-- business card fronts -->
<div class="piece card" style="left:6px;top:14px">
  <div class="brand" style="position:absolute;left:40px;top:38px"><span class="dot"></span>Ledgerway Partners, LLC</div>
  <div class="rule"></div>
</div>

<div class="piece card red" style="left:146px;top:14px">
  <div class="codes">DUNS NO. 052817634<br>NAICS CODES<br>541611<br>541214<br>541512<br>611430<br>561320</div>
  <div class="mark-circle" style="right:14px;top:18px;width:56px;height:56px;background:var(--faint)"></div>
</div>

<div class="piece card purple" style="left:286px;top:14px">
  <div class="codes">DUNS NO. 052817634<br>NAICS CODES<br>541611<br>541214<br>541512<br>611430<br>561320</div>
  <div class="mark-circle" style="right:14px;top:18px;width:56px;height:56px;background:var(--faint)"></div>
</div>

<!-- business card backs -->
<div class="piece card" style="left:6px;top:128px">
  <div style="position:absolute;left:10px;top:44px">
    <div class="name">Denise M. Holloway, CPP, PMP</div>
    <div class="role">Founder and CEO</div>
  </div>
  <div class="contact" style="position:absolute;left:10px;bottom:9px">dholloway@ledgerway-hq.com</div>
  <div class="rule"></div>
</div>

<div class="piece card" style="left:146px;top:128px">
  <div class="brand" style="position:absolute;left:10px;top:10px"><span class="dot"></span>Ledgerway Partners, LLC</div>
  <div class="contact" style="position:absolute;right:10px;top:38px;text-align:right">
    Tel (404) 555-0182<br>Fax (404) 555-0147<br>Cell (404) 555-0119<br>Skype hollodm7
  </div>
  <div class="contact" style="position:absolute;left:10px;bottom:8px">4812 Linwood Avenue NE Suite 210 Atlanta, GA 30318</div>
  <div class="rule"></div>
</div>

<div class="piece card" style="left:286px;top:128px">
  <div style="position:absolute;left:10px;top:10px">
    <div class="name">Denise M. Holloway, CPP, PMP</div>
    <div class="role">Founder and CEO</div>
  </div>
  <div class="contact" style="position:absolute;right:10px;top:38px;text-align:right">
    (404) 555-0182<br>(404) 555-0147<br>ledgerway-hq.com
  </div>
  <div class="rule purple"></div>
</div>

<!-- envelopes -->
<div class="piece env" style="left:428px;top:16px;background:#f4f4f4">
  <svg class="flap" viewBox="0 0 130 88" preserveAspectRatio="none" aria-hidden="true">
    <polygon points="0,0 130,0 65,40" fill="var(--red)"/>
    <polyline points="0,88 65,46 130,88" fill="none" stroke="#d6d6d6" stroke-width="1"/>
  </svg>
</div>
<div class="piece env" style="left:568px;top:16px;background:#f4f4f4">
  <svg class="flap" viewBox="0 0 130 88" preserveAspectRatio="none" aria-hidden="true">
    <polygon points="0,0 130,0 65,40" fill="var(--purple)"/>
    <polyline points="0,88 65,46 130,88" fill="none" stroke="#d6d6d6" stroke-width="1"/>
  </svg>
</div>
<div class="piece env" style="left:428px;top:128px">
  <div class="brand" style="position:absolute;left:8px;top:8px"><span class="dot"></span>Ledgerway Partners, LLC</div>
  <div class="contact" style="position:absolute;left:8px;top:22px">4812 Linwood Avenue NE Suite 210<br>Atlanta, GA 30318</div>
  <div class="rule"></div>
</div>
<div class="piece env" style="left:568px;top:128px">
  <div class="brand" style="position:absolute;left:8px;top:8px"><span class="dot"></span>Ledgerway Partners, LLC</div>
  <div class="mark-circle" style="right:10px;top:14px;width:60px;height:60px;background:var(--faint-dark)"></div>
  <div class="rule purple"></div>
</div>

<!-- letterheads -->
<div class="piece page" style="left:716px;top:14px">
  <div class="brand" style="position:absolute;left:12px;top:14px"><span class="dot"></span>Ledgerway Partners, LLC</div>
  <div class="contact" style="position:absolute;left:12px;bottom:10px">4812 Linwood Avenue NE Suite 210 Atlanta, GA 30318 · ledgerway-hq.com</div>
  <div class="rule"></div>
</div>
<div class="piece page" style="left:880px;top:14px">
  <div class="brand" style="position:absolute;left:12px;top:14px"><span class="dot"></span>Ledgerway Partners, LLC</div>
  <div class="mark-circle" style="left:30px;top:62px;width:90px;height:90px;background:var(--faint-dark)"></div>
  <div class="rule purple"></div>
</div>
<div class="piece page" style="left:1044px;top:14px">
  <div class="brand" style="position:absolute;left:12px;top:14px"><span class="dot"></span>Ledgerway Partners, LLC</div>
  <div class="contact" style="position:absolute;left:12px;bottom:10px">dholloway@ledgerway-hq.com · (404) 555-0182</div>
  <div class="rule"></div>
</div>

</body>
</html>
```